DrivPeak Agile Coaching Website

I need an updated website for www.drivpeak.example. I'm looking for a modern look. This is a professional site, but I don't want it to look "stuffy". It needs to have an element of fun and learning.

My services include:
Lean Agile Coaching
Lean Agile Training
Facilitation
Workshops
Consulting

Ideas this site should convey: collaboration, learning, teamwork, adaptability, flow, limited WIP, agility, Lean.

I would like to use some of my own photos and slide decks for content: http://www.deckvault.example/mornbeck/presentations

I would also like to include the Peerlinko recommendations I have from customers: https://www.peerlinko.example/in/mornbeck

Examples of sites I like:
http://www.quarrelmosswidget.example
http://www.forthsprintly.example

Target Market(s)

IT professionals, software development managers

Industry/Entity Type

It Company

Coding

Coded - Design and coding required

Font styles to use
Serif
Sans Serif

Requirements
Must have
• Original looking graphics and layout.
• My logo must be included in layout.
• Need to feature my blog content.
• Deliverable must be a WordPress theme that I can install.
• Responsive site.
Nice to have
• Use images from my slides on Deckvault if they make sense.

```html
<!DOCTYPE html>
<html lang="en">
<head>
<meta charset="utf-8">
<title>DrivPeak — Lean Agile Coaching</title>
<link rel="stylesheet" href="https://fonts.googleapis.com/css2?family=Montserrat:wght@400;500;600;700&family=Open+Sans:wght@400;600&display=swap">
<style>
:root{
  --green:#0fcc3f;
  --green-dark:#0bb236;
  --ink:#111111;
  --text:#555555;
  --muted:#777777;
  --white:#ffffff;
  --footer:#2a2a2a;
  --hero-a:#2b2b2b;
  --hero-b:#4a4a4a;
}
*{margin:0;padding:0;box-sizing:border-box}
html,body{width:827px;height:1200px;overflow:hidden;background:var(--white)}
body{position:relative;font-family:"Montserrat",sans-serif;color:var(--ink)}
.abs{position:absolute}

.site-header{position:absolute;left:0;top:0;width:827px;height:67px;border-top:2px solid var(--green);background:var(--white)}
.brand{position:absolute;left:91px;top:14px;display:flex;align-items:center;gap:6px;font-weight:700;font-size:29px;letter-spacing:-1px;color:var(--ink)}
.brand-mark{width:8px;height:28px;background:var(--green)}
.main-nav{position:absolute;top:29px;left:0;width:827px;font-size:7.5px;font-weight:500;letter-spacing:.2px}
.main-nav a{position:absolute;color:var(--ink);text-decoration:none}
.main-nav a.active{color:var(--green)}

.hero{position:absolute;left:0;top:67px;width:827px;height:328px;background:linear-gradient(90deg,#3a3a3a 0%,var(--hero-b) 30%,#1a1a1a 48%,#252525 75%,#121212 100%)}
.hero-title{position:absolute;top:127px;width:827px;text-align:center;color:var(--white);font-size:26px;font-weight:500;letter-spacing:.5px}
.hero-sub{position:absolute;top:174px;width:827px;text-align:center;color:#e8e8e8;font-family:"Open Sans",sans-serif;font-size:11px}
.btn{position:absolute;display:flex;align-items:center;justify-content:center;background:var(--green);color:var(--white);font-size:7px;font-weight:500;text-decoration:none;border-radius:2px}
.hero .btn{left:358px;top:212px;width:111px;height:32px;font-size:10px}
.dots{position:absolute;top:302px;left:400px;display:flex;gap:7px}
.dots i{width:5px;height:5px;border-radius:50%;background:#cfcfcf}
.dots i.on{background:var(--green)}

.section-title{position:absolute;width:827px;text-align:center;font-size:24px;font-weight:500;letter-spacing:.3px}
.welcome-text{position:absolute;left:91px;top:462px;width:644px;text-align:center;font-family:"Open Sans",sans-serif;font-size:7px;line-height:13px;color:var(--text)}

.services{position:absolute;left:0;top:583px;width:827px;height:215px}
.service{position:absolute;top:0;height:215px;color:var(--white);text-align:center}
.service.coaching{left:0;width:277px;background:var(--green)}
.service.training{left:277px;width:277px;background:linear-gradient(160deg,#5a6470,#3d434a 60%,#4b4f55)}
.service.facilitation{left:554px;width:273px;background:linear-gradient(160deg,#6d7480,#4a4f58 60%,#3c4047)}
.service svg{position:absolute;top:24px;left:50%;margin-left:-15px}
.service h3{position:absolute;top:74px;width:100%;font-size:16.5px;font-weight:500;letter-spacing:.3px}
.service p{position:absolute;top:107px;left:14px;right:14px;font-family:"Open Sans",sans-serif;font-size:7px;line-height:13px}
.service .btn{top:164px;left:50%;margin-left:-39px;width:78px;height:25px}
.service.coaching .btn{background:var(--ink)}
.slide-arrow{position:absolute;top:697px;width:21px;height:21px;background:#1b1b1b;display:flex;align-items:center;justify-content:center}

.post{position:absolute;top:889px;width:202px}
.post-image{height:131px;width:202px}
.post h4{margin-top:14px;font-size:13px;font-weight:500}
.post time{display:block;margin-top:3px;color:var(--green);font-family:"Open Sans",sans-serif;font-size:7.5px}
.post p{margin-top:8px;font-family:"Open Sans",sans-serif;font-size:7px;line-height:16px;color:var(--muted);text-align:justify}
.post .more{display:flex;align-items:center;gap:6px;margin-top:8px;color:var(--green);font-size:9px;font-weight:500}

.site-footer{position:absolute;left:0;top:1152px;width:827px;height:48px;background:var(--footer)}
.copyright{position:absolute;left:91px;top:19px;color:#e0e0e0;font-family:"Open Sans",sans-serif;font-size:7px}
.social{position:absolute;left:654px;top:18px;display:flex;gap:11px}
.social i{width:11px;height:11px;border-radius:50%;background:#8d8d8d}
</style>
</head>
<body>

<header class="site-header">
  <div class="brand"><span class="brand-mark"></span>DrivPeak</div>
  <nav class="main-nav">
    <a class="active" style="left:470px">HOME</a>
    <a style="left:524px">ABOUT</a>
    <a style="left:582px">SERVICES</a>
    <a style="left:649px">BLOG</a>
    <a style="left:700px">CONTACT</a>
  </nav>
</header>

<section class="hero" role="img" aria-label="Speaker presenting on stage in front of a projected slide about software process">
  <h1 class="hero-title">CLARITY, UNDERSTANDING, IMPROVEMENT</h1>
  <p class="hero-sub">Improving software development through alignment, visibility, knowledge, and discipline.</p>
  <a class="btn">READ MORE</a>
  <div class="dots"><i class="on"></i><i></i><i></i></div>
</section>

<h2 class="section-title" style="top:420px">WELCOME TO DRIVPEAK</h2>
<p class="welcome-text">DrivPeak is a company dedicated to improving the art and science of software development for both the consumers of software services and the professionals doing the work. Our primary focus is the marketplace and community where we live–the Kansas City metro area. Our specialty is helping software organizations learn about and implement Lean-Agile approaches to software development. This includes Kanban, Scrum and Agile team practices, and XP technical practices.</p>
<a class="btn" style="left:377px;top:517px;width:73px;height:26px">READ MORE</a>

<section class="services">
  <article class="service coaching">
    <svg width="30" height="34" viewBox="0 0 30 34" fill="none" stroke="#fff" stroke-width="1.2"><circle cx="15" cy="14" r="10"/><path d="M6 5a13 13 0 0 0 18 18M15 27v4M10 32h10"/></svg>
    <h3>LEAN AGILE COACHING</h3>
    <p>DrivPeak is a company dedicated to improving the art and science of software development for both the consumers of software services and the professionals doing the work.</p>
    <a class="btn">READ MORE</a>
  </article>
  <article class="service training" role="img" aria-label="Team raising hands together around a table">
    <svg width="30" height="34" viewBox="0 0 30 34" fill="none" stroke="#fff" stroke-width="1.2"><path d="M15 2c5 5 5 14 3 20h-6c-2-6-2-15 3-20z"/><circle cx="15" cy="11" r="2"/><path d="M12 18l-4 6h4M18 18l4 6h-4M15 24v6"/></svg>
    <h3>LEAN AGILE TRAINING</h3>
    <p>DrivPeak is a company dedicated to improving the art and science of software development for both the consumers of software services and the professionals doing the work.</p>
    <a class="btn">READ MORE</a>
  </article>
  <article class="service facilitation" role="img" aria-label="Business group meeting in an office">
    <svg width="30" height="34" viewBox="0 0 30 34" fill="none" stroke="#fff" stroke-width="1.2"><path d="M4 28L22 10M20 4a5 5 0 0 0 6 6l-3 3-6-6zM4 6l3-2 3 3-2 3zM10 9l16 16-3 3L7 12"/></svg>
    <h3>FACILITATION</h3>
    <p>DrivPeak is a company dedicated to improving the art and science of software development for both the consumers of software services and the professionals doing the work.</p>
    <a class="btn">READ MORE</a>
  </article>
</section>
<div class="slide-arrow" style="left:0"><svg width="6" height="9" viewBox="0 0 6 9"><path d="M5 1L1 4.5 5 8" stroke="#fff" fill="none"/></svg></div>
<div class="slide-arrow" style="left:806px"><svg width="6" height="9" viewBox="0 0 6 9"><path d="M1 1l4 3.5L1 8" stroke="#fff" fill="none"/></svg></div>

<h2 class="section-title" style="top:834px">RECENT BLOG</h2>

<article class="post" style="left:91px">
  <div class="post-image" role="img" aria-label="Workshop participants gathered around a table of cards" style="background:linear-gradient(135deg,#6b6660,#3a3632 60%,#8a8580)"></div>
  <h4>SPEAKING AT VELORA SUMMIT 2016</h4>
  <time>JUL 14, 2016</time>
  <p>I'm pleased to announce I'll be speaking at Velora Summit 2016 in Atlanta. My topic will be Minimal Viable Agile.</p>
  <a class="more">Read More <svg width="9" height="8" viewBox="0 0 9 8" fill="none" stroke="#0fcc3f"><path d="M0 4h8M5 1l3 3-3 3"/></svg></a>
</article>
<article class="post" style="left:312px">
  <div class="post-image" role="img" aria-label="Presenter pointing at a whiteboard chart" style="background:linear-gradient(135deg,#e6ecef,#cfd9dc 55%,#7bc6b9)"></div>
  <h4>SPEAKING AT VELORA SUMMIT 2016</h4>
  <time>JUL 14, 2016</time>
  <p>I'm pleased to announce I'll be speaking at Velora Summit 2016 in Atlanta. My topic will be Minimal Viable Agile.</p>
  <a class="more">Read More <svg width="9" height="8" viewBox="0 0 9 8" fill="none" stroke="#0fcc3f"><path d="M0 4h8M5 1l3 3-3 3"/></svg></a>
</article>
<article class="post" style="left:534px">
  <div class="post-image" role="img" aria-label="Colleagues working together at a laptop" style="background:linear-gradient(135deg,#f2f0ed,#d9d4cd 60%,#b9b2a8)"></div>
  <h4>SPEAKING AT VELORA SUMMIT 2016</h4>
  <time>JUL 14, 2016</time>
  <p>I'm pleased to announce I'll be speaking at Velora Summit 2016 in Atlanta. My topic will be Minimal Viable Agile.</p>
  <a class="more">Read More <svg width="9" height="8" viewBox="0 0 9 8" fill="none" stroke="#0fcc3f"><path d="M0 4h8M5 1l3 3-3 3"/></svg></a>
</article>

<footer class="site-footer">
  <p class="copyright">© Copyright 2016 drivpeak.example, All Rights Reserved</p>
  <div class="social"><i></i><i></i><i></i><i></i></div>
</footer>

</body>
</html>
```